Harlow Crest Holdings (Remodeling company) needs a logo and business card

We need a business card design for a new company. We "flip" upmarket houses (buy, remodel and sell) in the Austin, TX area. I'd like neutral colors (grey, white, gold black). I would like it to include a simple, clean logo. Our designs are modern and uncluttered and I would like that reflected in the business card design.

Target Market(s)

Young professionals, Families, Retirees. Our properties will sell for $750k+

Industry/Entity Type

Real Estate

Contact Information for Business Card

Harlow Crets Holdings
Mona Harlow
(979) 555 0142
Owner
Rolf Tandem
(512) 555 0176
Realtor

Logo Text

Harlow Crest Holdings

Font styles to use
Serif
Script

Requirements
Must have
• Simple, classic design
Nice to have
• Clean lines, modern look
Should not have
• Too traditionally

```html
<!DOCTYPE html>
<html lang="en">
<head>
<meta charset="utf-8">
<title>Harlow Crest Holdings — Business Card</title>
<link rel="stylesheet" href="https://fonts.googleapis.com/css2?family=Lobster+Two&family=Tinos&display=swap">
<style>
  :root {
    --backdrop: #d9d4cc;
    --card-black: #141414;
    --band-dark: #1f1f1f;
    --band-mid: #2c2c2c;
    --band-light: #5a5a5a;
    --crease: #3a3a3a;
    --gold: #d8b22c;
    --silver: #d6d6d6;
  }
  html, body {
    margin: 0;
    width: 1200px;
    height: 892px;
    overflow: hidden;
    background: var(--backdrop);
  }
  .card {
    position: absolute;
    left: 100px;
    top: 160px;
    width: 1000px;
    height: 572px;
    background: var(--card-black);
    border-radius: 6px;
    overflow: hidden;
    box-shadow: 0 10px 30px rgba(0,0,0,.35);
  }
  .card-waves {
    position: absolute;
    inset: 0;
  }
  .brand-name {
    position: absolute;
    left: 140px;
    top: 150px;
    margin: 0;
    font-family: "Lobster Two", cursive;
    font-weight: 400;
    font-size: 78px;
    color: var(--gold);
    line-height: 1;
  }
  .contact {
    position: absolute;
    left: 250px;
    margin: 0;
    font-family: "Tinos", serif;
    line-height: 1.1;
  }
  .contact-owner { top: 262px; }
  .contact-realtor { top: 392px; }
  .contact-name {
    display: block;
    font-size: 46px;
    color: var(--gold);
  }
  .contact-role,
  .contact-phone {
    display: block;
    font-size: 27px;
    color: var(--silver);
    margin-left: 36px;
  }
  .contact-role { margin-top: 4px; }
</style>
</head>
<body>
  <article class="card">
    <svg class="card-waves" width="1000" height="572" viewBox="0 0 1000 572" aria-hidden="true">
      <defs>
        <linearGradient id="topBand" x1="0" y1="0" x2="0" y2="1">
          <stop offset="0" stop-color="#161616"/>
          <stop offset="1" stop-color="#242424"/>
        </linearGradient>
        <radialGradient id="lowerGlow" cx="0.72" cy="0.72" r="0.6">
          <stop offset="0" stop-color="#6a6a6a"/>
          <stop offset="0.55" stop-color="#3a3a3a"/>
          <stop offset="1" stop-color="#1b1b1b"/>
        </radialGradient>
        <linearGradient id="midBand" x1="0" y1="0" x2="1" y2="1">
          <stop offset="0" stop-color="#202020"/>
          <stop offset="1" stop-color="#3c3c3c"/>
        </linearGradient>
      </defs>
      <rect class="band-top" width="1000" height="572" fill="url(#topBand)"/>
      <path class="band-middle" d="M0 250 C 280 140, 620 90, 1000 150 L1000 572 L0 572 Z" fill="url(#midBand)"/>
      <path class="band-lower" d="M0 330 C 300 300, 620 200, 1000 230 L1000 572 L0 572 Z" fill="url(#lowerGlow)"/>
      <path class="crease" d="M0 250 C 280 140, 620 90, 1000 150" fill="none" stroke="#0b0b0b" stroke-width="2"/>
      <path class="crease" d="M0 330 C 300 300, 620 200, 1000 230" fill="none" stroke="#101010" stroke-width="2"/>
      <path class="band-foot" d="M0 540 C 300 560, 700 520, 1000 480 L1000 572 L0 572 Z" fill="#1c1c1c" opacity=".6"/>
    </svg>

    <h1 class="brand-name">Harlow Crets Holdings</h1>

    <p class="contact contact-owner">
      <span class="contact-name">Mona Harlow</span>
      <span class="contact-role">Owner</span>
      <span class="contact-phone">(979) 555 0142</span>
    </p>

    <p class="contact contact-realtor">
      <span class="contact-name">Rolf Tandem</span>
      <span class="contact-role">Realtor</span>
      <span class="contact-phone">(512) 555 0176</span>
    </p>
  </article>
</body>
</html>
```